Life and Personal development life coach needs card design

I need a card design that matches the style and design of my website. I'd like to stay in the same color scheme. Please check out my website for ideas. www.brivelmorcott.com
I have had previous designs for this. I am wondering if you have access to those for more ideas??

```html
<!DOCTYPE html>
<html lang="en">
<head>
<meta charset="utf-8">
<title>Brivel Morcott – Life Coach Business Card</title>
<link rel="stylesheet" href="https://fonts.googleapis.com/css2?family=Gentium+Book+Plus:wght@400;700&display=swap">
<style>
  :root {
    --canvas-bg: #e6e6e6;
    --card-white: #ffffff;
    --ink: #111111;
    --lime: #a6c93a;
    --cyan: #37bcd9;
    --photo-light: #bdbdbd;
    --photo-dark: #2a2a2a;
    --card-shadow: rgba(0, 0, 0, 0.18);
  }
  * { box-sizing: border-box; margin: 0; padding: 0; }
  html, body {
    width: 1200px;
    height: 926px;
    overflow: hidden;
    background: var(--canvas-bg);
  }
  .canvas {
    position: relative;
    width: 1200px;
    height: 926px;
  }
  .card {
    position: absolute;
    left: 220px;
    width: 760px;
    height: 434px;
    background: var(--card-white);
    box-shadow: 0 6px 18px var(--card-shadow);
    overflow: hidden;
    font-family: "Gentium Book Plus", Georgia, serif;
    color: var(--ink);
  }

  /* Back of card */
  .card--back { top: 30px; }
  .card--back .title {
    position: absolute;
    top: 150px;
    width: 100%;
    text-align: center;
    font-size: 58px;
    font-weight: 400;
    letter-spacing: 9px;
  }
  .card--back .tagline {
    position: absolute;
    top: 236px;
    width: 100%;
    text-align: center;
    font-size: 26px;
    letter-spacing: 3px;
  }

  /* Front of card */
  .card--front { top: 492px; display: flex; }
  .portrait {
    width: 46%;
    height: 100%;
    background: linear-gradient(135deg, var(--photo-light) 0%, #7d7d7d 45%, var(--photo-dark) 100%);
  }
  .details {
    position: relative;
    width: 54%;
    height: 100%;
    padding: 44px 0 0 40px;
  }
  .label {
    display: inline-block;
    line-height: 1;
  }
  .name {
    background: var(--lime);
    font-size: 34px;
    padding: 6px 16px 6px 8px;
  }
  .name strong { font-weight: 700; }
  .role {
    display: block;
    width: fit-content;
    margin-top: 6px;
    background: var(--lime);
    font-size: 18px;
    letter-spacing: 2px;
    padding: 4px 40px 4px 8px;
  }
  .contact {
    position: absolute;
    left: 40px;
    bottom: 36px;
    list-style: none;
  }
  .contact li {
    width: fit-content;
    background: var(--cyan);
    font-size: 21px;
    padding: 4px 14px 4px 8px;
    margin-top: 8px;
  }
</style>
</head>
<body>
<main class="canvas">
  <section class="card card--back" aria-label="Card back">
    <h1 class="title">LIFE COACH</h1>
    <p class="tagline">Discover what is possible today!</p>
  </section>

  <section class="card card--front" aria-label="Card front">
    <div class="portrait" role="img" aria-label="Black and white portrait photograph of the life coach"></div>
    <div class="details">
      <span class="label name">Brivel <strong>Morcott</strong></span>
      <span class="label role">LIFE COACH</span>
      <ul class="contact">
        <li>P: 619-555-0187</li>
        <li>W: www.brivelmorcott.com</li>
        <li>E: hello@brivelmorcott.com</li>
      </ul>
    </div>
  </section>
</main>
</body>
</html>
```